Brenwick Drilling Inc. Business card design

Business card design for "Brenwick Drilling Inc. - Directional Drilling Services"

Address is:

Brenwick Drilling Inc.
512 - 73 Tolvane Crescent SW
Calgary, Alberta, Canada
T2K 4P8

Please incorporate the logo design into the card, thank you.

Target Market(s)

Oil & Gas and Drilling

Industry/Entity Type

Business

```html
<!DOCTYPE html>
<html lang="en">
<head>
<meta charset="utf-8">
<title>Brenwick Drilling Inc. – Business Card</title>
<link href="https://fonts.googleapis.com/css2?family=Cinzel:wght@400;600&display=swap" rel="stylesheet">
<style>
  :root {
    --backdrop: #d9d9d9;
    --card: #ffffff;
    --slate: #848589;
    --amber: #f6951e;
    --cream: #fdf2d8;
    --ring-dark: #55554f;
    --ring-light: #c9c7bd;
  }
  * { margin: 0; padding: 0; box-sizing: border-box; }
  html, body {
    width: 1200px; height: 860px; overflow: hidden;
    background: var(--backdrop);
  }
  .card {
    position: absolute; left: 161px; top: 161px;
    width: 878px; height: 538px;
    background: var(--card);
    font-family: "Cinzel", "Trajan Pro", serif;
  }
  .band-title {
    position: absolute; left: 0; top: 28px;
    width: 789px; height: 147px;
    background: var(--slate);
    clip-path: polygon(0 0, 100% 0, 100% 99px, 738px 100%, 0 100%);
  }
  .band-contact {
    position: absolute; left: 0; top: 191px;
    width: 789px; height: 324px;
    background: var(--amber);
    clip-path: polygon(0 0, 738px 0, 100% 49px, 100% 100%, 0 100%);
  }
  .company {
    position: absolute; left: 32px; top: 55px;
    color: var(--amber);
    font-size: 31px; font-weight: 600;
    letter-spacing: 0.1em; line-height: 44px;
    white-space: nowrap;
  }
  .contact-list {
    position: absolute; left: 32px; top: 243px;
    list-style: none;
    color: var(--slate);
    font-size: 27px; font-weight: 600;
    letter-spacing: 0.1em; line-height: 44px;
    white-space: nowrap;
  }
  .grommet {
    position: absolute; left: 759px; top: 132px;
    width: 102px; height: 102px; border-radius: 50%;
    background: var(--cream);
  }
  .grommet-ring {
    position: absolute; left: 13px; top: 13px;
    width: 76px; height: 76px; border-radius: 50%;
    background: radial-gradient(circle, var(--ring-dark) 46%, var(--ring-light) 62%, #8f8d85 80%, var(--ring-dark) 100%);
  }
  .grommet-hole {
    position: absolute; left: 20px; top: 20px;
    width: 36px; height: 36px; border-radius: 50%;
    background: var(--cream);
  }
</style>
</head>
<body>
  <section class="card">
    <div class="band-title"></div>
    <div class="band-contact"></div>
    <h1 class="company">
      Brenwick Drilling Inc.<br>
      Directional Drilling Services
    </h1>
    <ul class="contact-list">
      <li>Name: Lorem Ipsum</li>
      <li>Add:</li>
      <li>Tel: 000000000</li>
      <li>email:loremipsum@brenwickmail.com</li>
      <li>Website:www.brenwickdrilling.com</li>
    </ul>
    <div class="grommet">
      <div class="grommet-ring"><div class="grommet-hole"></div></div>
    </div>
  </section>
</body>
</html>
```